2024 Harwick Patrol Deputy's Statute Handbook

Cover, spine and back cover for our annual law manual. The overall size of the cover is 18.82 x 11 (with the .25 inch bleed it is 19.32 x 11.5) and the spine is 1.82 x 11 plus (1.82 x 11.5 with the bleed).
The book comes with a motor vehicle companion guide which will be 5" X 7" with spiral binding. The companion guide will have the same design with a slight twist related to motor vehicle law.

```html
<!DOCTYPE html>
<html lang="en">
<head>
<meta charset="UTF-8">
<title>2024 Harwick Patrol Deputy's Statute Handbook – Full Wrap</title>
<link href="https://fonts.googleapis.com/css2?family=Anton&family=Oswald:wght@400;700&family=Josefin+Sans:wght@700&display=swap" rel="stylesheet">
<style>
  :root {
    --backdrop: #d3d3d3;
    --navy: #0d1a6e;
    --navy-deep: #081150;
    --ink: #141414;
    --paper: #ffffff;
    --gold-light: #ffe23a;
    --gold: #f0a81c;
    --gold-dark: #b96a0c;
    --silver-light: #ffffff;
    --silver: #c9cdd2;
    --silver-dark: #7d848c;
    --light-pink: #e0306a;
    --light-violet: #4a2bb0;
  }
  * { box-sizing: border-box; margin: 0; padding: 0; }
  html, body { width: 1200px; height: 989px; overflow: hidden; background: var(--backdrop); }

  .wrap {
    position: absolute; left: 30px; top: 161px;
    width: 1140px; height: 666px; overflow: hidden;
    box-shadow: 0 12px 30px rgba(0,0,0,.25);
  }
  .panel { position: absolute; top: 0; height: 666px; overflow: hidden; }
  .panel--back { left: 0; width: 515px; }
  .panel--spine { left: 515px; width: 110px; border-left: 1px solid rgba(255,255,255,.15); border-right: 1px solid rgba(255,255,255,.15); }
  .panel--front { left: 625px; width: 515px; }

  .band { position: absolute; left: 0; width: 100%; }
  .band--photo { top: 0; height: 150px;
    background:
      radial-gradient(ellipse at 10% 35%, var(--light-pink) 0%, transparent 50%),
      radial-gradient(ellipse at 45% 20%, var(--light-violet) 0%, transparent 55%),
      linear-gradient(90deg, #2a0b28 0%, #150a3a 45%, #0e1a33 70%, #1c2a3d 100%); }
  .band--photo-cuffs { background: linear-gradient(180deg, #2b2b30, #121216); }
  .band--navy { top: 140px; height: 345px;
    background:
      radial-gradient(ellipse at 55% 55%, #1a2a92 0%, transparent 65%),
      linear-gradient(180deg, var(--navy-deep), var(--navy) 40%, var(--navy-deep)); }
  .band--base { top: 478px; height: 188px; background: linear-gradient(180deg, #1e1e1e, var(--ink)); }

  .tear { position: absolute; left: 0; width: 1140px; }
  .tear--top { top: 134px; height: 22px; }
  .tear--bottom { top: 462px; height: 28px; }

  /* front */
  .brand {
    position: absolute; top: 54px; left: 50%; transform: translateX(-50%);
    display: flex; align-items: center; gap: 8px; white-space: nowrap;
    background: var(--navy-deep); padding: 8px 14px;
    font-family: 'Oswald', sans-serif; font-weight: 700; font-size: 18px;
    letter-spacing: 1.5px; color: var(--gold);
  }
  .brand__dot { width: 14px; height: 14px; border-radius: 50%; background: var(--gold); }

  .title { position: absolute; left: 0; width: 100%; text-align: center; white-space: nowrap; font-family: 'Anton', sans-serif; display: block; }
  .title--rank {
    top: 214px; font-size: 56px; line-height: 1;
    background: linear-gradient(180deg, var(--silver-light) 0%, var(--silver) 45%, var(--silver-dark) 55%, var(--silver-light) 100%);
    -webkit-background-clip: text; background-clip: text; color: transparent;
  }
  .title--book {
    top: 282px; font-size: 60px; line-height: 1.1;
    background: linear-gradient(90deg, var(--gold-dark) 0%, var(--gold) 30%, var(--gold-light) 60%, var(--gold) 80%, var(--gold-dark) 100%);
    -webkit-background-clip: text; background-clip: text; color: transparent;
  }
  .title--year { top: 372px; font-size: 60px; line-height: 1; letter-spacing: 3px; color: var(--paper); }

  .guide { position: absolute; left: 38px; top: 520px; }
  .guide__state {
    font-family: 'Anton', sans-serif; font-size: 48px; line-height: 1;
    background: linear-gradient(180deg, var(--silver-light), var(--silver-dark) 60%, var(--silver));
    -webkit-background-clip: text; background-clip: text; color: transparent;
  }
  .guide__line { font-family: 'Oswald', sans-serif; font-weight: 700; font-size: 22px; line-height: 1.3; color: var(--silver); white-space: nowrap; }
  .guide__line em { font-style: normal; color: var(--gold-light); }
  .topics {
    position: absolute; left: 318px; top: 516px; list-style: none; white-space: nowrap;
    font-family: 'Oswald', sans-serif; font-weight: 400; font-size: 15px; line-height: 1.5; color: var(--paper);
  }
  .topics li::before { content: "• "; }
  .author {
    position: absolute; left: 0; width: 100%; top: 626px; text-align: center;
    font-family: 'Josefin Sans', sans-serif; font-weight: 700; font-size: 14px;
    letter-spacing: 1.2px; color: var(--paper);
  }

  /* spine */
  .spine__text {
    position: absolute; top: 160px; left: 50%; transform: translateX(-50%);
    writing-mode: vertical-rl; display: flex; flex-direction: row; align-items: flex-start; gap: 4px;
    white-space: nowrap;
  }
  .spine__title { font-family: 'Anton', sans-serif; font-size: 21px; line-height: 1.1; color: var(--paper); letter-spacing: .5px; }
  .spine__title em { font-style: normal; color: var(--gold); }
  .spine__author { font-family: 'Josefin Sans', sans-serif; font-weight: 700; font-size: 11px; letter-spacing: 1px; color: var(--paper); }
  .spine__brand {
    position: absolute; top: 520px; left: 50%; transform: translateX(-50%);
    writing-mode: vertical-rl; display: flex; align-items: center; gap: 8px; white-space: nowrap;
    font-family: 'Oswald', sans-serif; font-weight: 700; font-size: 14px; letter-spacing: 1.5px; color: var(--gold);
  }
  .spine__brand .brand__dot { width: 12px; height: 12px; }
</style>
</head>
<body>
  <main class="wrap">
    <section class="panel panel--back" aria-label="Back cover">
      <div class="band band--photo" role="img" aria-label="Police lights glowing red and violet at night"></div>
      <div class="band band--navy"></div>
      <div class="band band--base"></div>
    </section>

    <section class="panel panel--spine" aria-label="Spine">
      <div class="band band--photo band--photo-cuffs" role="img" aria-label="Steel handcuffs on a dark surface"></div>
      <div class="band band--navy"></div>
      <div class="band band--base"></div>
      <div class="spine__text">
        <span class="spine__title">PATROL DEPUTY'S <em>STATUTE HANDBOOK</em></span>
        <span class="spine__author">DANIEL R. WHITCOMBE, ESQ</span>
      </div>
      <div class="spine__brand"><span class="brand__dot"></span>LARKFIELD</div>
    </section>

    <section class="panel panel--front" aria-label="Front cover">
      <div class="band band--photo" role="img" aria-label="Police cruiser with flashing red and blue lights beside two uniformed officers"></div>
      <div class="band band--navy"></div>
      <div class="band band--base"></div>

      <div class="brand"><span class="brand__dot"></span>LARKFIELD CONSULTING</div>

      <h1>
        <span class="title title--rank">PATROL DEPUTY'S</span>
        <span class="title title--book">STATUTE HANDBOOK</span>
        <span class="title title--year">2024</span>
      </h1>

      <div class="guide">
        <div class="guide__state">HARWICK</div>
        <div class="guide__line">PATROL DEPUTY'S <em>GUIDE TO</em></div>
      </div>
      <ul class="topics">
        <li>Criminal Procedure</li>
        <li>Statutory Law</li>
        <li>Motor Vehicle Law</li>
        <li>Juvenile Law</li>
      </ul>
      <p class="author">DANIEL R. WHITCOMBE, ESQ</p>
    </section>

    <svg class="tear tear--top" viewBox="0 0 1140 22" preserveAspectRatio="none" aria-hidden="true">
      <polygon fill="#ffffff" points="0,8 60,3 120,10 180,4 240,11 300,4 360,10 420,3 480,11 540,5 600,10 660,3 720,11 780,4 840,10 900,3 960,11 1020,4 1080,10 1140,6 1140,17 1080,14 1020,19 960,13 900,20 840,14 780,19 720,13 660,20 600,14 540,19 480,13 420,20 360,14 300,19 240,13 180,20 120,14 60,19 0,15"/>
    </svg>
    <svg class="tear tear--bottom" viewBox="0 0 1140 28" preserveAspectRatio="none" aria-hidden="true">
      <polygon fill="#ffffff" points="0,10 60,14 120,7 180,15 240,8 300,16 360,6 420,14 480,8 540,15 600,5 660,13 720,7 780,15 840,6 900,13 960,5 1020,12 1080,4 1140,3 1140,16 1080,19 1020,22 960,17 900,24 840,18 780,23 720,17 660,24 600,18 540,23 480,17 420,24 360,18 300,23 240,17 180,24 120,18 60,24 0,20"/>
    </svg>
  </main>
</body>
</html>
```